Premium Gold Vodka Label Design

English ------------------- We need a label for a Vodka Bottle. Its a sparkling premium vodka with gold inside. The design should look premium. We tried it on our selves but it looks horrible. Therefore we need your help. The current name is corvelle K, but we are open for any better suggestion. We attached the selfmade design. The label will be printed on the bottle. We have other design jobs for you (logo, other sorts)! English ------------------------ We need a label for a vodka bottle. This is a premium vodka which is offset with gold. The design should look like this. We have tried so far and failed. That is why we need your support. The name is so far corvelle K. If you have better suggestions we would be pleased about other suggestions / ideas. In the appendix the failed design is stored. The label is to be applied by screen printing. In the case of good work follow-up projects are guaranteed (logo, other varieties, etc)!
Updates

Reason: We need more time for the decision.

Target Market(s)

USA

Colors

Designer to choose colors to be used in the design.

Requirements
Must have
• English ------------------------ The needed text is on our selfmade label that is attached. English ------------------------ The required texts are stored in the attached design.
Nice to have
• English ------------------------ Transparent places are allowed because we want to print the label on the bottom. English ------------------------ As the label is applied by screen printing, transparent areas are also possible.

```html
<!DOCTYPE html>
<html lang="en">
<head>
<meta charset="utf-8">
<title>corvelle K – Premium Gold Sparkling Vodka Label</title>
<link rel="stylesheet" href="https://fonts.googleapis.com/css2?family=Audiowide&family=Arimo:wght@400;700&display=swap">
<style>
  :root {
    --gold: #d29a33;
    --gold-light: #f3dfb0;
    --bronze: #8a4a2b;
    --label-black: #161616;
    --label-black-soft: #222222;
    --band-black: #050505;
    --text-white: #ffffff;
    --text-dark: #2b2b2b;
    --page: #ffffff;
  }
  html, body {
    margin: 0;
    padding: 0;
    width: 912px;
    height: 1200px;
    overflow: hidden;
    background: var(--page);
  }
  .label {
    position: relative;
    width: 912px;
    height: 1200px;
  }
  .label-shape {
    position: absolute;
    inset: 0;
  }
  .brand-band {
    position: absolute;
    left: 152px;
    top: 200px;
    width: 615px;
    height: 280px;
    background: var(--band-black);
    display: flex;
    align-items: center;
    justify-content: center;
  }
  .brand-name {
    font-family: "Audiowide", sans-serif;
    font-size: 100px;
    line-height: 1;
    color: var(--gold);
    letter-spacing: 1px;
    white-space: nowrap;
  }
  .karat-badge {
    position: absolute;
    left: 332px;
    top: 549px;
    width: 249px;
    height: 101px;
    background: var(--gold);
    display: flex;
    align-items: center;
    justify-content: center;
    font-family: "Audiowide", sans-serif;
    font-size: 66px;
    color: var(--text-dark);
  }
  .product-type {
    position: absolute;
    left: 0;
    right: 0;
    top: 722px;
    text-align: center;
    font-family: "Audiowide", sans-serif;
    font-size: 42px;
    line-height: 1.2;
    color: var(--text-white);
    letter-spacing: 1px;
    white-space: nowrap;
  }
  .spirit-name {
    position: absolute;
    left: 0;
    right: 0;
    top: 792px;
    text-align: center;
    font-family: "Audiowide", sans-serif;
    font-size: 88px;
    line-height: 1;
    color: var(--gold);
    letter-spacing: 3px;
  }
  .process {
    position: absolute;
    left: 0;
    right: 0;
    top: 924px;
    text-align: center;
    font-family: "Arimo", sans-serif;
    font-size: 61px;
    line-height: 1.1;
    color: var(--gold);
    white-space: nowrap;
  }
  .origin {
    position: absolute;
    left: 0;
    right: 0;
    top: 994px;
    text-align: center;
    font-family: "Arimo", sans-serif;
    font-size: 30px;
    color: var(--text-white);
  }
  .specs {
    position: absolute;
    top: 1062px;
    left: 0;
    right: 0;
    font-family: "Arimo", sans-serif;
    color: var(--text-white);
  }
  .specs span { position: absolute; white-space: nowrap; }
  .spec-abv { left: 249px; top: 9px; font-size: 22px; }
  .spec-volume { left: 0; right: 0; text-align: center; font-size: 35px; font-weight: 700; }
  .spec-proof { left: 579px; top: 9px; font-size: 22px; }
</style>
</head>
<body>
<div class="label">
  <svg class="label-shape" width="912" height="1200" viewBox="0 0 912 1200" aria-hidden="true">
    <defs>
      <linearGradient id="rim-gold" x1="0" y1="0" x2="1" y2="1">
        <stop offset="0" stop-color="#f6e7c4"/>
        <stop offset="0.25" stop-color="#d29a33"/>
        <stop offset="0.55" stop-color="#c98f34"/>
        <stop offset="0.8" stop-color="#8a4a2b"/>
        <stop offset="1" stop-color="#f3dfb0"/>
      </linearGradient>
      <linearGradient id="panel-fill" x1="0" y1="0" x2="0" y2="1">
        <stop offset="0" stop-color="#222222"/>
        <stop offset="0.5" stop-color="#161616"/>
        <stop offset="1" stop-color="#1e1e1e"/>
      </linearGradient>
    </defs>
    <rect class="rim" x="2" y="2" width="908" height="1196" rx="454" ry="380" fill="url(#rim-gold)"/>
    <rect class="panel" x="30" y="30" width="852" height="1140" rx="426" ry="356" fill="url(#panel-fill)" stroke="#000" stroke-width="2"/>
  </svg>

  <div class="brand-band">
    <div class="brand-name">corvelle K</div>
  </div>
  <div class="karat-badge">24KT</div>
  <div class="product-type">PREMIUM GOLD SPARKLING</div>
  <div class="spirit-name">VODKA</div>
  <div class="process">Distilled 8 Filtered</div>
  <div class="origin">Made in Germany</div>
  <div class="specs">
    <span class="spec-abv">40%Al. Vol.</span>
    <span class="spec-volume">200ml</span>
    <span class="spec-proof">80Proof</span>
  </div>
</div>
</body>
</html>
```